Sports Betting Business Consultant

After 21 years in corporate life. Will be continue as consultant/advisor in sports betting industry. Need a business card. Prefer an Zelvo format as layout. Elements; betting,ticket, sports types soccer, basketball, tennis etc , odds etc.

```html
<!DOCTYPE html>
<html lang="en">
<head>
<meta charset="utf-8">
<title>Deniz Arkan – Sports Advisor Business Card</title>
<link href="https://fonts.googleapis.com/css2?family=Lato:wght@300;400;700&display=swap" rel="stylesheet">
<style>
  :root {
    --backdrop: #2a2c30;
    --card: #121315;
    --card-edge: #1c1d20;
    --ink: #ffffff;
    --ink-soft: #b9bbbf;
    --rule: #4a4c50;
  }
  * { box-sizing: border-box; margin: 0; padding: 0; }
  html, body {
    width: 1200px;
    height: 900px;
    overflow: hidden;
    background: var(--backdrop);
    font-family: "Lato", sans-serif;
  }
  .stage {
    width: 1200px;
    height: 900px;
    display: flex;
    align-items: center;
    justify-content: center;
    gap: 90px;
  }
  .card {
    width: 340px;
    height: 580px;
    background: var(--card);
    border: 1px solid var(--card-edge);
    box-shadow: 0 18px 40px rgba(0,0,0,0.45);
    position: relative;
    color: var(--ink);
    text-align: center;
  }
  /* Front */
  .identity {
    position: absolute;
    top: 168px;
    left: 0;
    right: 0;
  }
  .identity-name {
    font-weight: 700;
    font-size: 28px;
    letter-spacing: 1px;
  }
  .identity-role {
    margin-top: 6px;
    font-weight: 300;
    font-size: 19px;
    color: var(--ink-soft);
  }
  .contact {
    position: absolute;
    top: 392px;
    left: 0;
    right: 0;
  }
  .contact-icons {
    display: flex;
    justify-content: center;
    gap: 6px;
  }
  .contact-rule {
    width: 190px;
    height: 1px;
    background: var(--rule);
    margin: 12px auto 16px;
  }
  .contact-line {
    font-weight: 400;
    font-size: 22px;
    color: var(--ink-soft);
    line-height: 1.4;
  }
  /* Back */
  .services {
    position: absolute;
    top: 120px;
    left: 0;
    right: 0;
  }
  .services-title {
    font-weight: 700;
    font-size: 27px;
    letter-spacing: 1px;
  }
  .services-rule {
    width: 90px;
    height: 1px;
    background: var(--rule);
    margin: 14px auto 18px;
  }
  .services-list {
    list-style: none;
    display: inline-block;
    text-align: left;
  }
  .services-item {
    font-weight: 400;
    font-size: 22px;
    color: var(--ink-soft);
    line-height: 1.45;
    display: flex;
    align-items: center;
    gap: 10px;
  }
  .services-item::before {
    content: "";
    width: 9px;
    height: 9px;
    border-radius: 50%;
    background: var(--ink);
  }
</style>
</head>
<body>
<main class="stage">
  <section class="card card-front">
    <div class="identity">
      <h1 class="identity-name">DENIZ ARKAN</h1>
      <p class="identity-role">Sports Advisor</p>
    </div>
    <div class="contact">
      <div class="contact-icons">
        <svg width="22" height="22" viewBox="0 0 22 22" aria-label="Phone">
          <circle cx="11" cy="11" r="10" fill="var(--ink)"/>
          <path d="M7 8.5c0-1 .6-1.6 1.4-1.6l1 1.7-.8.9c.5 1.1 1.4 2 2.5 2.5l.9-.8 1.7 1c0 .8-.6 1.4-1.6 1.4C9.4 13.6 7 11.4 7 8.5z" fill="var(--card)"/>
        </svg>
        <svg width="22" height="22" viewBox="0 0 22 22" aria-label="Email">
          <circle cx="11" cy="11" r="10" fill="var(--ink)"/>
          <rect x="6" y="7.5" width="10" height="7" fill="none" stroke="var(--card)" stroke-width="1.3"/>
          <path d="M6 7.5l5 4 5-4" fill="none" stroke="var(--card)" stroke-width="1.3"/>
        </svg>
      </div>
      <div class="contact-rule"></div>
      <p class="contact-line">+90 555 0148 207</p>
      <p class="contact-line">dnzarkan@mailpost.com</p>
    </div>
  </section>

  <section class="card card-back">
    <div class="services">
      <h2 class="services-title">SERVICES</h2>
      <div class="services-rule"></div>
      <ul class="services-list">
        <li class="services-item">Betting</li>
        <li class="services-item">Ticket</li>
        <li class="services-item">Soccer</li>
        <li class="services-item">Basketball</li>
        <li class="services-item">Tennis</li>
      </ul>
    </div>
  </section>
</main>
</body>
</html>
```